Brenmoor Group needs a business card

I would like the card to be simple but modern and elegant.
I like black and white.
or black and gold.
we are a private finance lender and also are involved in property and property developments.

please look at the business card photos i provided i would like B.G only one one side and all the other details on the other side use fonts that tie in with my theme.

Industry/Entity Type

Finance

Contact Information for Business Card

Brenmoor Group (B.G) Callum Brenmoor M: 0418396152 E: callumbren@quivomail.com

Font styles to use
Other font styles liked:
• Use fonts that would reflect our business

Colors
000000
ffffff

Requirements
Must have
• one side of details
• other side has either B.G or Brenmoor Group like in the photos provided

```html
<!DOCTYPE html>
<html lang="en">
<head>
<meta charset="utf-8">
<title>Brenmoor Group – Business Card</title>
<link rel="stylesheet" href="https://fonts.googleapis.com/css2?family=Montserrat:wght@400;500;700&display=swap">
<style>
  :root {
    --ink: #000000;
    --card-black: #1c1c1c;
    --paper: #ffffff;
    --backdrop: #d6d6d6;
    --text-soft: #2a2a2a;
    --rule: #4a4a4a;
  }
  * { margin: 0; padding: 0; box-sizing: border-box; }
  html, body {
    width: 1200px;
    height: 786px;
    overflow: hidden;
  }
  body {
    background: var(--backdrop);
    font-family: "Montserrat", Arial, sans-serif;
    display: flex;
    align-items: center;
    justify-content: center;
    gap: 60px;
  }
  .card {
    width: 520px;
    height: 297px;
    position: relative;
    flex: none;
    box-shadow: 0 10px 30px rgba(0, 0, 0, 0.18);
  }
  .card--front {
    background: var(--card-black);
  }
  .company-name {
    position: absolute;
    left: 64px;
    top: 50%;
    transform: translateY(-50%);
    color: var(--paper);
    font-weight: 500;
    font-size: 40px;
    letter-spacing: 1px;
    line-height: 1;
    white-space: nowrap;
  }
  .card--back {
    background: var(--paper);
    color: var(--ink);
  }
  .holder {
    position: absolute;
    top: 40px;
    right: 44px;
    width: 190px;
  }
  .holder__name {
    font-weight: 700;
    font-size: 14px;
    letter-spacing: 0.6px;
    text-transform: uppercase;
    white-space: nowrap;
    padding-bottom: 10px;
    border-bottom: 1px solid var(--rule);
  }
  .contact {
    position: absolute;
    left: 40px;
    bottom: 36px;
    list-style: none;
    font-size: 12.5px;
    font-weight: 400;
    letter-spacing: 0.8px;
    color: var(--text-soft);
    line-height: 1.7;
    white-space: nowrap;
  }
</style>
</head>
<body>
  <section class="card card--front" aria-label="Card front">
    <p class="company-name">Brenmoor Group</p>
  </section>

  <section class="card card--back" aria-label="Card back">
    <div class="holder">
      <p class="holder__name">Callum Brenmoor</p>
    </div>
    <ul class="contact">
      <li>M: 0418396152</li>
      <li>E: callumbren@quivomail.com</li>
    </ul>
  </section>
</body>
</html>
```